Briar Hollow

Need a site for a cbd dispensary texas theme. We sell all federal and legal hemp products

Target Market(s)

Cbd and other hemp derivatives

Industry/Entity Type

Hemp derivatives

Coding

Coded - Design and coding required

Number of Pages Required

3 page

Font styles to use
Sans Serif

Colors
0094D4
00A9DD
6FCCEA
C7EBF8
E9F6FB

Requirements
Must have
• Integration for bigcommerce shopping
Nice to have
• Easy layout for shopping

```html
<!DOCTYPE html>
<html lang="en">
<head>
<meta charset="utf-8">
<title>Briar Hollow — Hemp Dispensary</title>
<link href="https://fonts.googleapis.com/css2?family=Baloo+2:wght@700;800&family=Poppins:ital,wght@0,400;0,500;0,600;1,400;1,600&family=Saira:wght@500;600;700&display=swap" rel="stylesheet">
<style>
:root{
  --blue-deep:#0094D4;
  --blue:#00A9DD;
  --blue-mid:#6FCCEA;
  --blue-pale:#C7EBF8;
  --blue-mist:#E9F6FB;
  --ink:#2b2b2b;
  --muted:#6d6d6d;
  --white:#fff;
  --soft:#f6f7f8;
}
*{box-sizing:border-box;margin:0;padding:0}
html,body{width:1200px;height:5106px;overflow:hidden}
body{font-family:'Poppins',sans-serif;color:var(--ink);background:var(--white);position:relative}
.abs{position:absolute}
.heading{font-family:'Baloo 2',sans-serif;font-weight:800;font-style:italic;color:var(--blue-deep);letter-spacing:.5px}
.btn{position:absolute;display:flex;align-items:center;justify-content:center;background:var(--blue-deep);color:#fff;font-weight:600;font-style:italic;font-size:13px;border-radius:6px;box-shadow:0 4px 10px rgba(0,148,212,.35)}
.underline{position:absolute;height:4px;width:46px;background:var(--blue-mid);border-radius:2px;left:577px}
.dots{position:absolute;display:flex;gap:5px}
.dots i{width:11px;height:11px;border:1.5px solid var(--blue-deep);border-radius:50%;display:block}
.dots i.on{background:var(--blue-deep)}

.topbar{top:0;left:0;width:1200px;height:54px;font-size:11px;color:var(--blue-deep);font-weight:500}
.topbar span{position:absolute;top:20px}
.logo{position:absolute;font-family:'Saira',sans-serif;font-weight:700;font-size:25px;color:var(--blue-deep);display:flex;align-items:center;gap:8px}
.logo b{width:14px;height:14px;background:var(--blue-deep);display:block;border-radius:2px}
.search{top:74px;left:381px;width:451px;height:40px;background:#f1f1f1;border-radius:20px;font-size:11px;color:#888;padding:13px 20px}
.search .go{position:absolute;right:5px;top:5px;width:30px;height:30px;border-radius:50%;background:var(--blue-deep)}
.round-ic{position:absolute;width:34px;height:34px;border-radius:50%;background:var(--blue-deep)}
.nav{top:140px;left:0;width:1200px;height:58px;background:var(--blue-deep)}
.nav a{position:absolute;top:24px;color:#fff;font-size:11px;font-weight:600;text-decoration:none}
.hero{top:198px;left:0;width:1200px;height:681px;background:linear-gradient(180deg,#e4eef5 0%,#dfe9f0 45%,#c9c2b4 70%,#b49a7a 100%)}
.features{top:198px;left:132px;width:936px;height:58px;background:#fff;border-radius:0 0 26px 26px;box-shadow:0 4px 10px rgba(0,0,0,.05)}
.feat{position:absolute;top:12px;font-size:11px}
.feat b{display:block;color:var(--blue-deep);font-weight:500;font-size:11px}
.feat em{font-style:normal;font-size:10px;color:#444}
.feat svg{position:absolute;left:-58px;top:-2px}
.hero-title{top:312px;left:0;width:1200px;text-align:center;font-size:56px}
.hero-text{top:392px;left:180px;width:840px;text-align:center;font-size:12px;line-height:27px;color:#333}
.blueline{top:879px;left:0;width:1200px;height:8px;background:var(--blue)}
.promo{position:absolute;top:905px;height:336px;color:#fff;font-family:'Saira',sans-serif;overflow:hidden}
.promo .big{position:absolute;font-weight:700;font-size:36px;letter-spacing:1px}
.promo .sub{position:absolute;font-weight:500;font-size:23px;line-height:34px;letter-spacing:1px}
.promo .cta{position:absolute;font-weight:700;font-size:13px}
.promo .shot{position:absolute;border-radius:4px}
.rule{top:1319px;left:100px;width:1000px;height:2px;background:#ccc}
.card-img{position:absolute;top:1438px;width:224px;height:262px;background:linear-gradient(160deg,#f3f3f3,#e5e7e6)}
.card-img.raised{background:#fff;box-shadow:0 2px 10px rgba(0,0,0,.15)}
.card-img .art{position:absolute;left:30px;top:50px;width:164px;height:160px;border-radius:50%;}
.pname{position:absolute;top:1716px;width:224px;text-align:center;font-weight:600;font-style:italic;font-size:16px}
.stars{position:absolute;top:1744px;width:224px;text-align:center;color:#f5a623;font-size:12px;letter-spacing:2px}
.pdesc{position:absolute;top:1762px;width:224px;text-align:center;font-size:12px;color:var(--muted)}
.price{position:absolute;top:1785px;width:224px;text-align:center;font-family:'Saira',sans-serif;font-weight:600;font-size:25px;color:var(--blue-deep)}
.cart{position:absolute;top:1833px;width:224px;height:44px;border-radius:5px;background:var(--blue-mist);color:var(--blue-deep);display:flex;align-items:center;justify-content:center;font-size:13px;font-weight:600;font-style:italic}
.cart.on{background:var(--blue-deep);color:#fff;box-shadow:0 4px 10px rgba(0,148,212,.35)}
.member{top:2012px;left:0;width:1200px;height:553px;background:linear-gradient(90deg,#b6e2ef 0%,#a9dcec 50%,#8fd0e6 100%)}
.member-art{top:2012px;left:630px;width:570px;height:553px;background:linear-gradient(135deg,#d9a4a0 0%,#c98e8b 45%,#8fd0e6 75%)}
.member-title{top:2104px;left:131px;font-size:39px;line-height:40px}
.member-text{top:2232px;left:131px;width:460px;font-size:11px;line-height:28px;color:#333}
.field{position:absolute;background:#fff;border-radius:22px;font-size:11px;color:#888;padding:0 20px;display:flex;align-items:center}
.about{top:2565px;left:0;width:1200px;height:681px;background:linear-gradient(180deg,#eef0f1 0%,#e9ecec 55%,#c9d6b7 75%,#9cb56a 100%)}
.about-card{top:2648px;left:133px;width:934px;height:384px;background:rgba(255,255,255,.85);border-radius:16px}
.about-title{top:2682px;left:0;width:1200px;text-align:center;font-size:38px}
.about-text{top:2770px;left:180px;width:840px;text-align:center;font-size:11.5px;line-height:28px;color:#333}
.tcard{position:absolute;top:3424px;width:331px;height:226px;background:#fff;box-shadow:0 2px 12px rgba(0,0,0,.12)}
.tcard q{position:absolute;left:22px;top:16px;color:var(--blue-deep);font-size:22px;font-weight:600;quotes:none}
.tcard p{position:absolute;left:22px;top:44px;width:290px;font-size:12px;font-style:italic;line-height:28px;color:#333}
.tcard .av{position:absolute;left:22px;top:168px;width:46px;height:46px;border-radius:50%;background:linear-gradient(180deg,#bfc6cc,#7d8890)}
.tcard .who{position:absolute;left:90px;top:181px;font-size:14px;font-weight:600;font-style:italic;color:var(--blue-deep)}
.tcard.fade{opacity:.55}
.insta{top:3734px;left:0;width:1200px;height:851px;background:var(--soft)}
.shot{position:absolute}
.footer{top:4585px;left:0;width:1200px;height:521px;background:linear-gradient(180deg,#1fa3dc,#0a8fcc)}
.fcol{position:absolute;color:#fff;font-size:11.5px}
.fcol h4{font-size:13px;font-weight:600;letter-spacing:.5px;margin-bottom:12px}
.fcol li{list-style:none;line-height:28px}
.fcol li::before{content:"»";margin-right:8px}
.hr{position:absolute;height:1px;background:rgba(255,255,255,.5)}
.soc{position:absolute;top:5025px;width:30px;height:30px;border-radius:50%;background:#fff}
.pay{position:absolute;top:5032px;width:32px;height:21px;border-radius:3px;background:#fff}
</style>
</head>
<body>

<div class="abs topbar">
  <span style="left:148px">FAST FREE SHIPPING OVER $49 &nbsp;|&nbsp; CALL US RIGHT NOW ON ( 123 456 7890 )</span>
  <span style="left:829px">USD ▾</span>
  <span style="left:903px">English ▾</span>
  <span style="left:995px">Track Order</span>
</div>

<div class="logo" style="top:78px;left:135px"><b></b>Briar Hollow</div>
<div class="abs search">Search the products<span class="go"></span>
  <svg class="abs" style="right:13px;top:12px" width="15" height="15" viewBox="0 0 16 16"><circle cx="7" cy="7" r="4.5" fill="none" stroke="#fff" stroke-width="2"/><path d="M10.5 10.5L14 14" stroke="#fff" stroke-width="2"/></svg>
</div>
<span class="round-ic" style="top:77px;left:858px"></span>
<svg class="abs" style="top:86px;left:866px" width="18" height="16" viewBox="0 0 18 16"><path d="M2 8h9M8 4l4 4-4 4" stroke="#fff" stroke-width="2" fill="none"/><path d="M13 2h3v12h-3" stroke="#fff" stroke-width="2" fill="none"/></svg>
<span class="abs" style="top:87px;left:901px;font-size:11px;font-weight:600">SIGN IN</span>
<span class="round-ic" style="top:77px;left:963px"></span>
<svg class="abs" style="top:86px;left:971px" width="18" height="16" viewBox="0 0 18 16"><path d="M1 2h3l2 8h9l2-6H5" stroke="#fff" stroke-width="2" fill="none"/><circle cx="7" cy="14" r="1.5" fill="#fff"/><circle cx="14" cy="14" r="1.5" fill="#fff"/></svg>
<span class="abs" style="top:76px;left:1008px;font-size:10px;font-weight:600">MY CART</span>
<span class="abs" style="top:84px;left:1008px;font-family:'Saira',sans-serif;font-weight:700;font-size:22px;color:var(--blue-deep)">00:00</span>

<nav class="abs nav">
  <a style="left:246px">HOME</a><a style="left:326px">ABOUT US</a><a style="left:430px">OUR PRODUCTS</a>
  <a style="left:568px">TESTIMONIALS</a><a style="left:703px">OFFERS</a><a style="left:794px">BLOGS</a><a style="left:877px">CONTACT US</a>
</nav>

<div class="abs hero" role="img" aria-label="Flat lay of hemp leaves, herb spoons, capsules, wooden slices, pine cones and tincture bottles"></div>
<div class="abs features">
  <div class="feat" style="left:110px"><svg width="44" height="32" viewBox="0 0 44 32"><rect x="2" y="6" width="24" height="18" fill="none" stroke="#0094D4" stroke-width="2"/><path d="M26 12h9l6 6v6H26z" fill="none" stroke="#0094D4" stroke-width="2"/><circle cx="10" cy="27" r="3" fill="#fff" stroke="#0094D4" stroke-width="2"/><circle cx="34" cy="27" r="3" fill="#fff" stroke="#0094D4" stroke-width="2"/></svg><b>FREE DELIVERY</b><em>Lorem ipsum dolor sit amet</em></div>
  <div class="feat" style="left:434px"><svg width="44" height="32" viewBox="0 0 44 32"><rect x="2" y="6" width="24" height="18" fill="none" stroke="#0094D4" stroke-width="2"/><path d="M26 12h9l6 6v6H26z" fill="none" stroke="#0094D4" stroke-width="2"/><circle cx="10" cy="27" r="3" fill="#fff" stroke="#0094D4" stroke-width="2"/><circle cx="34" cy="27" r="3" fill="#fff" stroke="#0094D4" stroke-width="2"/></svg><b>SHIPPING WITHIN 24H</b><em>Lorem ipsum dolor sit amet</em></div>
  <div class="feat" style="left:756px"><svg width="44" height="32" viewBox="0 0 44 32"><rect x="2" y="6" width="24" height="18" fill="none" stroke="#0094D4" stroke-width="2"/><path d="M26 12h9l6 6v6H26z" fill="none" stroke="#0094D4" stroke-width="2"/><circle cx="10" cy="27" r="3" fill="#fff" stroke="#0094D4" stroke-width="2"/><circle cx="34" cy="27" r="3" fill="#fff" stroke="#0094D4" stroke-width="2"/></svg><b>30 DAYS RETURN</b><em>Lorem ipsum dolor sit amet</em></div>
</div>
<h1 class="abs heading hero-title">Welcome To Briar Hollow</h1>
<p class="abs hero-text">Lorem ipsum dolor sit amet, consectetur adipiscing elit, sed do eiusmod tempor incididunt ut labore et dolore magna aliqua. Quis ipsum suspendisse ultrices gravida. Risus commodo viverra maecenas accumsan lacus vel facilisis.</p>
<div class="btn" style="top:459px;left:498px;width:204px;height:54px">Shop Our Collection</div>
<div class="dots" style="top:818px;left:570px"><i class="on"></i><i></i><i></i><i></i></div>
<div class="abs blueline"></div>

<div class="promo" style="left:24px;width:369px;background:linear-gradient(160deg,#16a5dc,#0c95d2)">
  <div class="shot" style="left:120px;top:130px;width:230px;height:200px;background:linear-gradient(180deg,#1a7fb8,#1b3f7a 60%,#3a6d2f)" role="img" aria-label="Blue glass bottles with hemp leaves"></div>
  <div class="big" style="left:26px;top:28px">20% OFF</div>
  <div class="sub" style="left:26px;top:76px;font-size:22px">LOREM IPSUM DOLOR</div>
  <div class="cta" style="left:26px;top:120px">SHOP NOW</div>
</div>
<div class="promo" style="left:416px;width:368px;background:linear-gradient(160deg,#7fd2ee,#5fc4e6)">
  <div class="shot" style="left:120px;top:30px;width:200px;height:230px;background:linear-gradient(180deg,#3b3b3b,#5f6f3a 60%,#7fa14a)" role="img" aria-label="Dropper bottle with hemp buds"></div>
  <div class="big" style="left:24px;top:28px">SAVE 20%</div>
  <div class="sub" style="left:24px;top:82px;font-size:32px;line-height:46px">ON EVERY<br>ORDER</div>
  <div class="btn" style="left:16px;top:265px;width:180px;height:52px;box-shadow:none">Shop Our Products</div>
</div>
<div class="promo" style="left:805px;width:369px;background:linear-gradient(160deg,#2a8ed0,#1a75b8 60%,#2c8fd0)" role="img" aria-label="Blue tinted hemp product on a wooden table">
  <div class="big" style="left:34px;top:80px">BIG SALE</div>
  <div class="sub" style="left:34px;top:132px">LOREM IPSUM DOLOR<br>SIT AMET, CONSECTETUR</div>
  <div class="cta" style="left:34px;top:222px">SHOP NOW</div>
</div>

<div class="abs rule"></div>
<h2 class="abs heading" style="top:1340px;left:0;width:1200px;text-align:center;font-size:38px">Our Hemp Products</h2>
<div class="underline" style="top:1400px"></div>

<div class="card-img" style="left:113px" role="img" aria-label="CBD dropper bottle with vape pen"><div class="art" style="background:radial-gradient(circle,#7a4a1e 0%,#c9a36a 45%,transparent 70%)"></div></div>
<div class="card-img raised" style="left:363px" role="img" aria-label="Hemp cookies with cannabis leaf"><div class="art" style="background:radial-gradient(circle,#a26a35 0%,#5f8f3a 45%,transparent 70%)"></div></div>
<div class="card-img" style="left:613px" role="img" aria-label="Hemp oil bowl with seeds and leaf"><div class="art" style="background:radial-gradient(circle,#e8c52a 0%,#6fa040 45%,transparent 70%)"></div></div>
<div class="card-img" style="left:863px" role="img" aria-label="Bowl of green hemp pills with leaf"><div class="art" style="background:radial-gradient(circle,#3d2a1e 0%,#6aa54c 45%,transparent 70%)"></div></div>

<div class="pname" style="left:113px">Product Name</div><div class="pname" style="left:363px">Product Name</div><div class="pname" style="left:613px">Product Name</div><div class="pname" style="left:863px">Product Name</div>
<div class="stars" style="left:113px">★★★★★</div><div class="stars" style="left:363px">★★★★★</div><div class="stars" style="left:613px">★★★★★</div><div class="stars" style="left:863px">★★★★★</div>
<div class="pdesc" style="left:113px">Lorem ipsum dolor</div><div class="pdesc" style="left:363px">Lorem ipsum dolor</div><div class="pdesc" style="left:613px">Lorem ipsum dolor</div><div class="pdesc" style="left:863px">Lorem ipsum dolor</div>
<div class="price" style="left:113px">$ 120:00</div><div class="price" style="left:363px">$ 120:00</div><div class="price" style="left:613px">$ 120:00</div><div class="price" style="left:863px">$ 120:00</div>
<div class="cart" style="left:113px">Add To Cart</div><div class="cart on" style="left:363px">Add To Cart</div><div class="cart" style="left:613px">Add To Cart</div><div class="cart" style="left:863px">Add To Cart</div>
<div class="dots" style="top:1919px;left:570px"><i class="on"></i><i></i><i></i><i></i></div>

<div class="abs member"></div>
<div class="abs member-art" role="img" aria-label="Pink gift boxes with ribbons and dropper bottles"></div>
<h2 class="abs heading member-title">Our Membership<br><span style="color:#244a6b">Subscribe</span></h2>
<p class="abs member-text">Lorem ipsum dolor sit amet, consectetur adipiscing elit, sed do eiusmod tempor incididunt ut labore et dolore magna aliqua. Quis ipsum suspendisse ultrices gravida. Risus commodo viverra.</p>
<div class="field" style="top:2336px;left:131px;width:452px;height:41px">Enter The Email</div>
<div class="btn" style="top:2408px;left:131px;width:202px;height:54px">Subscribe</div>

<div class="abs about" role="img" aria-label="Hemp leaves and glass oil bottles on a marble surface"></div>
<div class="abs about-card"></div>
<h2 class="abs heading about-title">About Briar Hollow</h2>
<p class="abs about-text">Lorem ipsum dolor sit amet, consectetur adipiscing elit, sed do eiusmod tempor incididunt ut labore et dolore magna aliqua. Quis ipsum suspendisse ultrices gravida. Risus commodo viverra maecenas accumsan lacus vel facilisis. Lorem ipsum dolor sit amet, consectetur adipiscing elit, sed do eiusmod tempor incididunt ut labore et dolore magna aliqua. Ut enim ad minim veniam, quis nostrud exercitation ullamco laboris nisi ut aliquip ex ea commodo consequat. Duis aute irure dolor in reprehenderit in voluptate velit esse cillum dolore eu fugiat nulla pariatur. Excepteur sint occaecat cupidatat non proident, sunt in culpa qui officia deserunt mollit anim id est laborum.</p>
<div class="btn" style="top:2927px;left:498px;width:204px;height:54px">Learn More About Us</div>

<h2 class="abs heading" style="top:3316px;left:0;width:1200px;text-align:center;font-size:38px">What Our People Says about Us</h2>
<div class="underline" style="top:3376px"></div>
<svg class="abs" style="top:3508px;left:130px" width="44" height="50" viewBox="0 0 44 50"><path d="M2 10h38M30 2l10 8-10 8" stroke="#0094D4" stroke-width="2.5" fill="none"/><path d="M42 40H4M14 32L4 40l10 8" stroke="#0094D4" stroke-width="2.5" fill="none"/></svg>
<div class="tcard" style="left:222px"><q>“</q><p>Sed ut perspiciatis unde omnis iste natus err or sit voluptatem accusantium doloremque laudantium, totam rem aperiam, eaque ipsa quae ab illo inventore .</p><span class="av" role="img" aria-label="Customer portrait"></span><span class="who">John Deo</span></div>
<div class="tcard" style="left:585px"><q>“</q><p>Sed ut perspiciatis unde omnis iste natus err or sit voluptatem accusantium doloremque laudantium, totam rem aperiam, eaque ipsa quae ab illo inventore .</p><span class="av" role="img" aria-label="Customer portrait"></span><span class="who">John Deo</span></div>
<div class="tcard fade" style="left:948px"><q>“</q><p>Sed ut perspiciatis unde omnis iste natus err or sit voluptatem accusantium doloremque laudantium, totam rem aperiam, eaque ipsa quae ab illo inventore .</p><span class="av" role="img" aria-label="Customer portrait"></span><span class="who">John Deo</span></div>

<div class="abs insta"></div>
<h2 class="abs heading" style="top:3804px;left:0;width:1200px;text-align:center;font-size:38px">Follow Our Feed</h2>
<div class="underline" style="top:3864px"></div>
<div class="shot" style="left:149px;top:3904px;width:296px;height:188px;background:linear-gradient(135deg,#5a3a22,#a27a4a 60%,#7b5a3a)" role="img" aria-label="Amber bottles with hemp leaf on wood"></div>
<div class="shot" style="left:453px;top:3904px;width:296px;height:188px;background:linear-gradient(135deg,#eef0ea,#c9d6b2 60%,#8aa55a)" role="img" aria-label="Dropper bottle with hemp leaves on white"></div>
<div class="shot" style="left:756px;top:3904px;width:296px;height:188px;background:linear-gradient(135deg,#e7ead8,#b9c48a 60%,#8b7a45)" role="img" aria-label="Dropper over oil glass with seeds"></div>
<div class="shot" style="left:149px;top:4102px;width:600px;height:188px;background:linear-gradient(135deg,#f4f1e8,#e3c84a 45%,#a27a3a 80%)" role="img" aria-label="Row of hemp oil bottles with seeds"></div>
<div class="shot" style="left:756px;top:4102px;width:296px;height:386px;background:linear-gradient(160deg,#1f7a68,#2a8c77 50%,#d9d3c1)" role="img" aria-label="Hemp cosmetics, soap and powders on green"></div>
<div class="shot" style="left:149px;top:4300px;width:296px;height:188px;background:linear-gradient(135deg,#6a4a2a,#c07a45 50%,#5a7a3a)" role="img" aria-label="Hemp cookies with leaves"></div>
<div class="shot" style="left:453px;top:4300px;width:296px;height:188px;background:linear-gradient(135deg,#3a2a1a,#c98a2a 55%,#6a4a2a)" role="img" aria-label="Oil bottles on dark background"></div>

<footer class="abs footer" role="img" aria-label="Blue wooden background with faint hemp leaves"></footer>
<h3 style="top:4654px;left:0;width:1200px;text-align:center;font-size:29px;position:absolute;font-family:'Saira',sans-serif;font-weight:600;color:#fff;letter-spacing:1px">JOIN OUR MAILING LIST</h3>
<div class="field" style="top:4716px;left:290px;width:599px;height:45px;border-radius:23px;padding-left:44px">Enter Email Here</div>
<div class="btn" style="top:4719px;left:740px;width:146px;height:39px;border-radius:20px;font-style:normal;box-shadow:none">Subscribe</div>
<div class="hr" style="top:4801px;left:64px;width:1072px"></div>
<div class="logo" style="top:4912px;left:130px;color:#fff;font-size:32px"><b style="background:#fff"></b>Briar Hollow</div>
<div class="fcol" style="top:4830px;left:407px"><h4>QUICK LINKS</h4><ul><li>Home</li><li>Our Products</li><li>Testimonials</li><li>Offers</li><li>Blogs</li></ul></div>
<div class="fcol" style="top:4830px;left:643px"><h4>LEGAL</h4><ul><li>Privacy Policy</li><li>Terms &amp; Conditions</li><li>About Us</li><li>Contact Us</li><li>Cookie Policy</li></ul></div>
<div class="fcol" style="top:4830px;left:841px;line-height:28px"><h4>CONTACT US</h4>
  <div style="padding-left:20px;position:relative"><svg class="abs" style="left:0;top:7px" width="11" height="14" viewBox="0 0 11 14"><path d="M5.5 0a5 5 0 0 1 5 5c0 4-5 9-5 9S.5 9 .5 5a5 5 0 0 1 5-5z" fill="#fff"/><circle cx="5.5" cy="5" r="2" fill="#0a8fcc"/></svg>123 Lorem ipsum dolor sit amet<br>consectetur adipiscing.</div>
  <div style="padding-left:20px;position:relative;margin-top:8px"><svg class="abs" style="left:0;top:8px" width="12" height="12" viewBox="0 0 12 12"><path d="M2 0l3 3-1.5 2a7 7 0 0 0 3.5 3.5L9 7l3 3-2 2C5 12 0 7 0 2z" fill="#fff"/></svg>123 456 7890</div>
  <div style="padding-left:20px;position:relative;margin-top:12px"><svg class="abs" style="left:0;top:9px" width="13" height="10" viewBox="0 0 13 10"><rect width="13" height="10" fill="#fff"/><path d="M0 0l6.5 5L13 0" stroke="#0a8fcc" fill="none"/></svg>hello@briarhollow-shop.com</div>
</div>
<div class="hr" style="top:5012px;left:64px;width:1072px"></div>
<span class="soc" style="left:157px"></span><span class="soc" style="left:201px"></span><span class="soc" style="left:245px"></span><span class="soc" style="left:289px"></span>
<span class="abs" style="top:5034px;left:410px;color:#fff;font-size:11.5px">© Copyright 2021 <i>Briar Hollow</i> &nbsp; | &nbsp; All Rights Reserved</span>
<span class="pay" style="left:911px"></span><span class="pay" style="left:949px"></span><span class="pay" style="left:987px"></span><span class="pay" style="left:1031px"></span>
<span class="abs" style="top:5070px;left:1112px;color:#fff;font-size:10px">v 1.0</span>

</body>
</html>
```